Attorney Business Card

I need a business card that looks professional yet modern. I am an Attorney. , I need a professional yet modern business card for my law practice. My logo and information have been uploaded. , I need a business card that looks professional yet modern. I am an Attorney. , I need a professional yet modern business card for my law practice. My logo and information have been uploaded.

Industry/Entity Type

Business

Requirements
Must have
• My logo which has been uploaded , my logo , My logo which has been uploaded , my logo

```html
<!DOCTYPE html>
<html lang="en">
<head>
<meta charset="utf-8">
<title>Marlowe Law Firm – Business Cards</title>
<link href="https://fonts.googleapis.com/css2?family=Open+Sans:wght@600;700&display=swap" rel="stylesheet">
<style>
  :root{
    --stage:#e9e7e4;
    --ink-dark:#1d1d1f;
    --orange:#f6a02a;
    --paper:#ffffff;
    --cyan:#4ec8f2;
    --cyan-soft:#63cdf0;
    --teal-a:#62e0dc;
    --teal-b:#bdf4f6;
    --navy:#1a2838;
    --curl-dark:#1f1f22;
    --curl-light:#c9ccd0;
  }
  *{margin:0;padding:0;box-sizing:border-box}
  html,body{width:1200px;height:720px;overflow:hidden}
  body{background:var(--stage);font-family:"Open Sans",Arial,sans-serif;position:relative}
  .card{position:absolute;width:446px;height:256px;overflow:hidden;box-shadow:0 4px 12px rgba(0,0,0,.18)}
  .card svg{position:absolute;inset:0;width:100%;height:100%}
  .front--dark{left:118px;top:86px;background:var(--ink-dark)}
  .front--light{left:622px;top:86px;background:var(--paper)}
  .back--dark{left:116px;top:382px;background:var(--ink-dark)}
  .back--light{left:618px;top:382px;background:linear-gradient(90deg,var(--teal-b),var(--teal-a) 45%,var(--teal-a))}
  .url{position:absolute;top:26px;right:22px;font-weight:700;font-size:15px;letter-spacing:.2px}
  .front--dark .url{color:var(--ink-dark)}
  .front--light .url{color:var(--paper)}
  .brand-name{font-family:"Open Sans",Arial,sans-serif;font-weight:700;text-anchor:middle}
  .contact{position:absolute;left:256px;top:28px;font-size:12.5px;line-height:17px;text-transform:uppercase}
  .back--dark .contact{color:var(--orange);font-weight:600}
  .back--light .contact{color:var(--navy);font-weight:700}
  .contact p{margin-bottom:17px}
  .contact .title{padding-left:14px;display:block}
</style>
</head>
<body>

<section class="card front--dark">
  <svg viewBox="0 0 446 256" preserveAspectRatio="none">
    <defs>
      <linearGradient id="curlDark" x1="0" y1="0" x2="1" y2="1">
        <stop offset="0" stop-color="var(--curl-dark)"/>
        <stop offset="1" stop-color="var(--curl-light)"/>
      </linearGradient>
    </defs>
    <polygon points="232,0 446,0 446,256" fill="var(--orange)"/>
    <path d="M232,0 C200,90 205,200 236,256 L446,256 Z" fill="url(#curlDark)"/>
    <circle cx="120" cy="128" r="74" fill="none" stroke="var(--orange)" stroke-width="6"/>
    <text class="brand-name" x="120" y="124" font-size="19" fill="var(--orange)">MARLOWE</text>
    <text class="brand-name" x="120" y="146" font-size="19" fill="var(--orange)">LAW FIRM</text>
  </svg>
  <div class="url">WWW.MLFIRM.COM</div>
</section>

<section class="card front--light">
  <svg viewBox="0 0 446 256" preserveAspectRatio="none">
    <defs>
      <linearGradient id="curlLight" x1="0" y1="0" x2="1" y2="1">
        <stop offset="0" stop-color="var(--curl-dark)"/>
        <stop offset="1" stop-color="var(--curl-light)"/>
      </linearGradient>
    </defs>
    <polygon points="232,0 446,0 446,256" fill="var(--cyan)"/>
    <path d="M232,0 C200,90 205,200 236,256 L446,256 Z" fill="url(#curlLight)"/>
    <circle cx="120" cy="128" r="74" fill="none" stroke="var(--cyan)" stroke-width="6"/>
    <text class="brand-name" x="120" y="124" font-size="19" fill="var(--cyan)">MARLOWE</text>
    <text class="brand-name" x="120" y="146" font-size="19" fill="var(--cyan)">LAW FIRM</text>
  </svg>
  <div class="url">WWW.MLFIRM.COM</div>
</section>

<section class="card back--dark">
  <svg viewBox="0 0 446 256" preserveAspectRatio="none">
    <circle cx="92" cy="124" r="150" fill="none" stroke="var(--orange)" stroke-width="22"/>
    <text class="brand-name" x="100" y="118" font-size="30" fill="var(--orange)">MARLOWE</text>
    <text class="brand-name" x="100" y="154" font-size="30" fill="var(--orange)">LAW FIRM</text>
  </svg>
  <div class="contact">
    <p>Daniel Marlowe, Esq.<span class="title">Attorney at Law</span></p>
    <p>2210 Crestline Ave.<br>Suite 400<br>Westbrook, CA 90418</p>
    <p>555.210.4400 Tel<br>555.210.4488 Fax<br>555.730.2261 Mobile</p>
    <p>daniel@mlfirm.com</p>
  </div>
</section>

<section class="card back--light">
  <svg viewBox="0 0 446 256" preserveAspectRatio="none">
    <circle cx="92" cy="124" r="150" fill="none" stroke="var(--cyan-soft)" stroke-width="22" opacity=".85"/>
    <text class="brand-name" x="100" y="118" font-size="30" fill="var(--cyan-soft)">MARLOWE</text>
    <text class="brand-name" x="100" y="154" font-size="30" fill="var(--cyan-soft)">LAW FIRM</text>
  </svg>
  <div class="contact">
    <p>Daniel Marlowe, Esq.<span class="title">Attorney at Law</span></p>
    <p>2210 Crestline Ave.<br>Suite 400<br>Westbrook, CA 90418</p>
    <p>555.210.4400 Tel<br>555.210.4488 Fax<br>555.730.2261 Mobile</p>
    <p>daniel@mlfirm.com</p>
  </div>
</section>

</body>
</html>
```